Business card design - landscaping industry

Hello! We are very creative when it comes to landscape design but when it comes to designing business cards - not so much. We could use some help to come up with a design which is professional but fun. We are based in Grand Rapids, MI and work with high end properties for new landscape design and install. We are looking to have a template made for business card for a couple of us on staff.

You can get the flavor of our color scheme from our attached logo. We probably would want to highlight the green but also include some of the blue maybe.

Target Market(s)

We work with residential homeowners here in West Michigan. Very nice people by and large.

Industry/Entity Type

Landscaping

Contact Information for Business Card

The card should be standard size with round edges maybe?

Font styles to use
Serif
Sans Serif
Decorative

Requirements
Must have
• Must haves:
• 1. Address: 4817 Birchwell Meadow Lane SE, Grand Rapids, Michigan 49582
• 2. Phone: 616.555.0187
• 3. Email: company@larkhollowyard.com
• 4. URL: www.larkhollowyard.com
• 5. Names/Titles: (1) Dennis Harlow, President (2) Tomas Belvin, Director of Field Services
Nice to have
• On the back side of the card, we are thinking it would make sense to have a short listing of services offered...
• Landscape design & installation, Professional lawn maintenance, Spring & fall leaf cleanup, Irrigation system installation & maintenance, Snowplowing, Fertilizer & weed control, Tree maintenance and removal, Landscape bed maintenance
Should not have
• Our hope is that the design won't be too ostentatious. We are looking for professional and attractive.

```html
<!DOCTYPE html>
<html lang="en">
<head>
<meta charset="utf-8">
<title>Lark Hollow Landscaping – Business Cards</title>
<link href="https://fonts.googleapis.com/css2?family=Montserrat:wght@400;500&family=Libre+Baskerville:wght@700&display=swap" rel="stylesheet">
<style>
  :root {
    --backdrop: #9c9c9c;
    --card: #fbfbfb;
    --ink: #2e2e2e;
    --muted: #4a4a4a;
    --green: #36a152;
    --green-deep: #2f9148;
    --blue: #3f78c0;
    --blue-light: #9cbfe3;
  }
  * { box-sizing: border-box; margin: 0; padding: 0; }
  html, body { width: 1200px; height: 900px; overflow: hidden; }
  body {
    background: radial-gradient(ellipse at 50% 45%, #b2b2b2 0%, var(--backdrop) 75%);
    font-family: "Montserrat", Arial, sans-serif;
    position: relative;
  }
  .card {
    position: absolute;
    width: 560px;
    height: 320px;
    background: var(--card);
    border-radius: 18px;
    overflow: hidden;
    box-shadow: 0 14px 30px rgba(0,0,0,0.28);
  }
  .card--back { left: 60px; top: 90px; }
  .card--front { left: 580px; top: 490px; }

  .wordmark {
    display: flex;
    align-items: center;
    gap: 10px;
    font-weight: 500;
    color: var(--ink);
    letter-spacing: 0.22em;
    text-transform: uppercase;
    font-size: 15px;
    line-height: 20px;
  }
  .wordmark__dot {
    flex: none;
    width: 12px; height: 12px; border-radius: 50%;
    background: var(--green);
  }

  /* back side */
  .card--back .wordmark { position: absolute; left: 0; right: 0; top: 62px; justify-content: center; }
  .services {
    position: absolute; left: 20px; right: 20px; top: 150px;
    text-align: center;
    font-size: 13px;
    line-height: 26px;
    color: var(--muted);
  }
  .services .sep { color: var(--green); padding: 0 6px; }

  /* front side */
  .card--front .wordmark { position: absolute; left: 34px; top: 60px; }
  .holder { position: absolute; right: 40px; top: 52px; text-align: right; }
  .holder__name {
    font-family: "Libre Baskerville", Georgia, serif;
    font-weight: 700; color: var(--green); font-size: 22px;
  }
  .holder__title { font-size: 15px; color: var(--ink); margin-top: 2px; }
  .address {
    position: absolute; left: 60px; top: 140px;
    font-size: 13.5px; line-height: 20px; color: var(--ink);
  }
  .contact {
    position: absolute; left: 60px; top: 194px;
    list-style: none; font-size: 13.5px; line-height: 22px; color: var(--ink);
  }
  .contact li { display: flex; align-items: center; gap: 8px; }
  .contact svg { width: 13px; height: 13px; fill: var(--green); }
  .wave { position: absolute; left: 0; top: 0; width: 560px; height: 320px; }
  .url {
    position: absolute; right: 28px; top: 266px;
    color: #fff; font-size: 13px; letter-spacing: 0.02em;
  }
</style>
</head>
<body>

<section class="card card--back" aria-label="Card back with services">
  <div class="wordmark"><span class="wordmark__dot"></span><span>Lark Hollow<br>Landscaping</span></div>
  <p class="services">
    Landscape design &amp; installation<span class="sep">|</span>Professional lawn maintenance<br>
    Spring &amp; fall leaf cleanup<span class="sep">|</span>Irrigation system installation &amp; maintenance<br>
    Snowplowing<span class="sep">|</span>Fertilizer &amp; weed control<span class="sep">|</span>Tree maintenance and removal<br>
    Landscape bed maintenance
  </p>
</section>

<section class="card card--front" aria-label="Card front with contact details">
  <svg class="wave" viewBox="0 0 560 320" aria-hidden="true">
    <path d="M0,320 L0,302 C200,300 330,276 420,208 C470,170 510,148 560,140 L560,320 Z" fill="var(--green)"/>
    <path d="M0,296 C200,294 326,270 414,202 C466,162 508,140 560,132" fill="none" stroke="var(--blue)" stroke-width="3"/>
    <path d="M40,292 C210,286 324,262 410,194 C462,154 506,132 560,124" fill="none" stroke="var(--blue-light)" stroke-width="2"/>
  </svg>
  <div class="wordmark"><span class="wordmark__dot"></span><span>Lark Hollow<br>Landscaping</span></div>
  <div class="holder">
    <div class="holder__name">Dennis Harlow</div>
    <div class="holder__title">President</div>
  </div>
  <p class="address">4817 Birchwell Meadow Lane SE<br>Grand Rapids, Michigan 49582</p>
  <ul class="contact">
    <li><svg viewBox="0 0 24 24"><path d="M6.6 10.8a15 15 0 0 0 6.6 6.6l2.2-2.2a1 1 0 0 1 1-.25 11.4 11.4 0 0 0 3.6.6 1 1 0 0 1 1 1V20a1 1 0 0 1-1 1A17 17 0 0 1 3 4a1 1 0 0 1 1-1h3.5a1 1 0 0 1 1 1c0 1.25.2 2.45.6 3.6a1 1 0 0 1-.25 1z"/></svg>616.555.0187</li>
    <li><svg viewBox="0 0 24 24"><path d="M2 5h20v14H2z"/><path d="M2 5l10 8 10-8" fill="none" stroke="#fff" stroke-width="1.6"/></svg>company@larkhollowyard.com</li>
  </ul>
  <div class="url">www.larkhollowyard.com</div>
</section>

</body>
</html>
```